Retail and Ecommerce Archery Shop needs new Home Page Design

We need a homepage design created for an existing company named Redhollow Bowsport Hub. They sell various types of Archery equipment for both Bow hunting and Target shooting both in store and online. They offer shooting lessons, have an indoor archery shooting range with memberships available, and have their own line of bowstrings. For color scheme, use the current home page as inspiration. The Homepage Template has links to specific images, if any other images are needed, stock images are acceptable.

Current Website: https://rhbowsporthub.com/

Customer Avatar: https://files.quillnest.net/page/d/4Tq8Wm2RbXk9LpZ3vNc7HyF1gJd6sKe5uA0oVtB2/view?mode=shared

Core Message Canvas: https://files.quillnest.net/tables/d/7Hm_482rTz906R3k21wLuNy8Pq0Zc47bd5jS2X_vW/view?mode=shared

Homepage Template-Use this worksheet as the structue of the homepage: https://files.quillnest.net/page/d/9xkpWvRfa2B5nT7eLcM3JsYq0HdG8oUiZbN4/view?mode=shared

```html
<!DOCTYPE html>
<html lang="en">
<head>
<meta charset="utf-8">
<title>Redhollow Bowsport Hub – Home</title>
<link href="https://fonts.googleapis.com/css2?family=Playfair+Display:wght@400;500&family=Poppins:wght@400;500;600&display=swap" rel="stylesheet">
<style>
:root{
  --red:#ed1c24;
  --deep-red:#a3161c;
  --blue:#1b86c4;
  --gold:#d9b21f;
  --ink:#1d1d1d;
  --muted:#555;
  --light:#f4f4f4;
  --footer:#262626;
  --white:#fff;
  --badge-dark:#222;
}
*{box-sizing:border-box;margin:0;padding:0}
html,body{width:1200px;height:3136px;overflow:hidden}
body{position:relative;font-family:"Poppins",sans-serif;color:var(--ink);background:var(--white)}
.abs{position:absolute}
.topbar{left:0;top:0;width:1200px;height:36px;background:var(--deep-red);color:#fff;font-size:11px;text-align:center;line-height:36px;letter-spacing:.2px}
.nav{left:0;top:36px;width:1200px;height:74px;background:var(--white)}
.nav a{position:absolute;top:27px;font-size:14px;color:var(--ink);text-decoration:none;font-weight:500}
.brand{position:absolute;left:520px;top:18px;width:160px;text-align:center;font-family:"Playfair Display",serif;font-size:17px;line-height:19px;color:var(--deep-red)}
.brand .dot{display:inline-block;width:10px;height:10px;border-radius:50%;background:var(--gold);margin-right:6px}
.hero{left:0;top:110px;width:1200px;height:624px;background:linear-gradient(160deg,#3a4335 0%,#1f2620 45%,#2f2a33 100%)}
.hero-tag{left:0;top:578px;width:1200px;text-align:center;color:#fff;font-size:17px}
.btn{position:absolute;height:36px;border-radius:18px;color:#fff;font-size:13px;font-weight:600;text-align:center;line-height:36px;text-transform:uppercase}
.btn-blue{background:var(--blue)}
.btn-red{background:var(--red)}
.section-title{position:absolute;left:0;width:1200px;text-align:center;font-family:"Playfair Display",serif;font-size:38px;font-weight:400;color:var(--ink)}
.rule{position:absolute;height:2px;background:var(--gold)}
.services{left:0;top:734px;width:1200px;height:578px;background:var(--light)}
.services p{position:absolute;left:120px;top:126px;width:960px;text-align:center;font-size:15.5px;line-height:29px;color:#333}
.partner{position:absolute;width:301px;height:133px;background:#fff;box-shadow:0 2px 8px rgba(0,0,0,.08)}
.partner .badge{position:absolute}
.video{left:0;top:1312px;width:1200px;height:530px;background:radial-gradient(circle at 55% 45%,#5a3a2c 0%,#2b2523 45%,#141414 100%)}
.welcome{left:0;top:1842px;width:1200px;height:641px;background:#fff}
.shop-photo{position:absolute;left:100px;top:142px;width:370px;height:426px;background:linear-gradient(170deg,#6b6256 0%,#3a342f 55%,#1f1c1a 100%)}
.welcome .copy{position:absolute;left:494px;top:140px;width:606px}
.copy h3{font-size:16px;font-weight:600;color:var(--ink);margin-bottom:6px}
.copy p{font-size:12.8px;line-height:25.5px;color:#555;margin-bottom:10px;text-align:justify}
.news{left:0;top:2483px;width:1200px;height:298px;background:linear-gradient(180deg,#1d8ccc,#1576b0)}
.news h2{position:absolute;left:0;top:64px;width:1200px;text-align:center;font-family:"Playfair Display",serif;font-size:36px;font-weight:400;line-height:43px;color:#fff}
.news p{position:absolute;left:0;top:160px;width:1200px;text-align:center;font-size:15px;color:#e8f3fa}
.news-field{position:absolute;left:248px;top:195px;width:704px;height:43px;background:#fff;border-radius:22px}
.news-field span{position:absolute;left:26px;top:13px;font-size:12px;color:#666}
.news-field .btn{top:0;right:0;width:156px;height:43px;line-height:43px;border-radius:22px}
.footer{left:0;top:2781px;width:1200px;height:355px;background:var(--footer);color:#d8d8d8}
.footer h4{position:absolute;top:56px;font-size:17px;font-weight:600;color:#fff;letter-spacing:.3px}
.footer ul{position:absolute;top:98px;list-style:none;font-size:15px;line-height:34.5px}
.contact{position:absolute;left:325px;top:98px;font-size:15px;line-height:20px}
.contact div{display:flex;gap:8px;margin-bottom:18px}
.social{position:absolute;top:102px;width:42px;height:42px;border:1.5px solid #d8d8d8;border-radius:50%}
.copyright{position:absolute;left:0;top:316px;width:1200px;text-align:center;font-size:15px}
.overlay{left:0;top:0;width:1200px;height:3136px;background:rgba(0,0,0,.62)}
.modal{left:240px;top:167px;width:719px;height:410px;background:#fff;border-radius:4px;overflow:hidden}
.modal-photo{position:absolute;left:0;top:0;width:359px;height:410px;background:linear-gradient(180deg,#b9cfe2 0%,#8fa2b0 40%,#4c5150 75%,#2e2f2c 100%)}
.modal h2{position:absolute;left:359px;top:108px;width:360px;text-align:center;font-family:"Playfair Display",serif;font-size:36px;font-weight:400}
.modal p{position:absolute;left:359px;top:160px;width:360px;text-align:center;font-size:12.5px}
.modal-field{position:absolute;left:375px;top:197px;width:329px;height:41px;border:1px solid #ccc;border-radius:21px;text-align:center;line-height:39px;font-size:13.5px;color:#333}
.modal .btn{left:375px;top:250px;width:329px;height:42px;line-height:42px;border-radius:21px;font-size:13.5px}
.close{position:absolute;left:678px;top:18px}
</style>
</head>
<body>

<div class="abs topbar">NEW REWARDS PROGRAM IN EFFECT! START EARNING POINTS TO REDEEM ON PURCHASES! CURRENT LEAD TIME ON STRINGS: 3 WEEKS</div>

<header class="abs nav">
  <a style="left:104px">SHOP</a>
  <a style="left:184px">ABOUT US</a>
  <a style="left:295px">RANGE</a>
  <a style="left:384px">PRO SHOP</a>
  <div class="brand"><span class="dot"></span>Redhollow<br>Bowsport Hub</div>
  <a style="left:717px">ELECTRIC BOWSTRINGS</a>
  <svg class="abs" style="left:896px;top:28px" width="14" height="16" viewBox="0 0 14 16"><circle cx="7" cy="5" r="3.5" fill="none" stroke="#333" stroke-width="1.3"/><path d="M1 15c0-4 3-6 6-6s6 2 6 6" fill="none" stroke="#333" stroke-width="1.3"/></svg>
  <a style="left:917px;top:30px">MY ACCOUNT</a>
  <svg class="abs" style="left:1030px;top:24px" width="24" height="24" viewBox="0 0 24 24"><circle cx="10" cy="10" r="7.5" fill="none" stroke="#222" stroke-width="2"/><path d="M15.5 15.5l6 6" stroke="#222" stroke-width="2.4" stroke-linecap="round"/></svg>
  <svg class="abs" style="left:1064px;top:22px" width="32" height="28" viewBox="0 0 32 28"><path d="M2 4h4l4 14h14l3-10H8" fill="#222" stroke="#222" stroke-width="2" stroke-linejoin="round"/><circle cx="12" cy="23" r="2.3" fill="#222"/><circle cx="22" cy="23" r="2.3" fill="#222"/><circle cx="26" cy="5" r="5" fill="var(--blue)"/></svg>
</header>

<section class="abs hero" role="img" aria-label="Bowhunter drawing a bow in a tall wildflower meadow at dusk"></section>
<div class="abs hero-tag">•Top-Notch Equipment • Expertise • Unmatched Support</div>
<div class="btn btn-blue" style="left:379px;top:628px;width:214px">Indoor Archery Range</div>
<div class="btn btn-red" style="left:606px;top:628px;width:214px">Shop Our Bows</div>

<section class="abs services">
  <h2 class="section-title" style="top:54px">We Are a Full-Service Archery Pro Shop</h2>
  <span class="rule" style="left:284px;top:100px;width:652px"></span>
  <p>Our services include Bow setup and sizing, D-loop and peep sight installs, accessory installs, and setup, cam/limb swaps, string swaps, paper tuning, 2nd/3rd axis adjustments, replacement parts, arrow building, tuning, and much more!</p>
  <div class="partner" style="left:125px;top:215px" role="img" aria-label="Partner brand badge"><span class="badge" style="left:56px;top:28px;width:190px;height:78px;background:var(--deep-red)"></span></div>
  <div class="partner" style="left:448px;top:215px" role="img" aria-label="Partner brand badge"><span class="badge" style="left:36px;top:22px;width:230px;height:90px;border-radius:50%;background:var(--badge-dark)"></span></div>
  <div class="partner" style="left:773px;top:215px" role="img" aria-label="Partner brand badge"><span class="badge" style="left:25px;top:28px;width:252px;height:76px;border-radius:10px;background:#3a3a3a"></span></div>
  <div class="partner" style="left:125px;top:371px" role="img" aria-label="Partner brand badge"><span class="badge" style="left:46px;top:30px;width:210px;height:74px;background:var(--badge-dark)"></span></div>
  <div class="partner" style="left:448px;top:371px" role="img" aria-label="Partner brand badge"><span class="badge" style="left:36px;top:32px;width:230px;height:70px;background:#2c2c2c"></span></div>
  <div class="partner" style="left:773px;top:371px" role="img" aria-label="Partner brand badge"><span class="badge" style="left:50px;top:20px;width:200px;height:94px;background:#b08a17"></span></div>
</section>

<section class="abs video" role="img" aria-label="Close-up of hands serving a custom red bowstring">
  <svg class="abs" style="left:564px;top:234px" width="72" height="72" viewBox="0 0 72 72"><circle cx="36" cy="36" r="34" fill="rgba(255,255,255,.25)"/><circle cx="36" cy="36" r="26" fill="#fff"/><path d="M31 27l13 9-13 9z" fill="var(--red)"/></svg>
  <h2 class="section-title" style="top:382px;color:#e9d9a0">Our Custom Electric Bowstrings</h2>
  <span class="rule" style="left:328px;top:428px;width:544px"></span>
  <div class="btn btn-red" style="left:459px;top:448px;width:282px">Shop Our Custom Bowstrings</div>
</section>

<section class="abs welcome">
  <h2 class="section-title" style="top:61px">Welcome to your local Archery Shop</h2>
  <span class="rule" style="left:302px;top:107px;width:596px"></span>
  <div class="shop-photo" role="img" aria-label="Shop technician tuning a compound bow at the workbench in front of the accessory wall"></div>
  <div class="copy">
    <h3>Looking for a new Bow setup?</h3>
    <p>Our custom bow-fitting process will be perfect for you. We get you set up the right way, the first time! We will get your measurements, check your shot, and make sure you leave feeling confident with your new Bow!</p>
    <h3>Looking to make some improvements to your current archery setup?</h3>
    <p>We have access to almost all of the popular archery accessories on the market! We don't sell anything we wouldn't use ourselves so come on in and talk with our shop experts to figure out what will work best for you.</p>
    <h3>Are you looking to improve your shot? Reserve some time on our range!</h3>
    <p>Before you step into the field to take your first shot of the season, take time to go to the range. Archery, like any skill, requires practice &amp; diligence to develop a consistent &amp; confident shot. We have a 12-lane 20-yard indoor range in the shop. Daily Range and memberships are available. We also offer bow rental and lessons.</p>
  </div>
  <div class="btn btn-red" style="left:495px;top:529px;width:226px">Range Informaiton</div>
</section>

<section class="abs news">
  <h2>Join Our Archery Community: Exclusive Deals,<br>Tips, and Updates Straight to Your Inbox!</h2>
  <span class="rule" style="left:284px;top:145px;width:652px"></span>
  <p>Join today &amp; stay up-to-date on new product releases, shop promotions, and our archery newsletters</p>
  <div class="news-field"><span>Enter Your Email Address</span><div class="btn btn-red">Sign Up</div></div>
</section>

<footer class="abs footer">
  <h4 style="left:100px">NAVIGATION</h4>
  <ul style="left:100px"><li>Shop</li><li>About Us</li><li>Range</li><li>Pro Shop</li><li>Electric Bowstrings</li></ul>
  <h4 style="left:325px">CONTACT US</h4>
  <div class="contact">
    <div><svg width="14" height="18" viewBox="0 0 14 18"><path d="M7 1a6 6 0 0 0-6 6c0 4.5 6 10 6 10s6-5.5 6-10a6 6 0 0 0-6-6z" fill="#d8d8d8"/><circle cx="7" cy="7" r="2.3" fill="var(--footer)"/></svg><span>412 Ridgeline Rd, Cedar Falls,<br>KS 66000</span></div>
    <div><svg width="16" height="16" viewBox="0 0 16 16"><path d="M3 1l3 3-1.5 2a9 9 0 0 0 5.5 5.5L12 10l3 3-2 2C7 15 1 9 1 3z" fill="none" stroke="#d8d8d8" stroke-width="1.4"/></svg><span>(555)-014-0277</span></div>
    <div><svg width="18" height="14" viewBox="0 0 18 14"><rect x="1" y="1" width="16" height="12" fill="none" stroke="#d8d8d8" stroke-width="1.4"/><path d="M1 1l8 7 8-7" fill="none" stroke="#d8d8d8" stroke-width="1.4"/></svg><span>hello@rhbowsporthub.com</span></div>
  </div>
  <h4 style="left:690px">USEFULL LINK</h4>
  <ul style="left:690px"><li>Help</li><li>Shipping Policy</li><li>Privacy Policy</li><li>Refund Policy</li><li>Terms of Service</li></ul>
  <h4 style="left:896px">FOLLOW US</h4>
  <span class="social" style="left:896px"></span>
  <span class="social" style="left:950px"></span>
  <span class="social" style="left:1003px"></span>
  <span class="social" style="left:1057px"></span>
  <div class="copyright">©Copyright ©2023 Redhollow Bowsport Hub LLC. All Rights Reserved.</div>
</footer>

<div class="abs overlay"></div>

<div class="abs modal">
  <div class="modal-photo" role="img" aria-label="Two bowhunters climbing a rocky ridge with snowy mountains behind"></div>
  <svg class="close" width="24" height="24" viewBox="0 0 24 24"><path d="M4 4l16 16M20 4L4 20" stroke="#111" stroke-width="2.6" stroke-linecap="round"/></svg>
  <h2>Join The Club</h2>
  <span class="rule" style="left:406px;top:146px;width:266px"></span>
  <p>Get insider access to new products and promotions</p>
  <div class="modal-field">Email Address</div>
  <div class="btn btn-red">Sign Up</div>
</div>

</body>
</html>
```